Concierge Healthcare Business Card Design and Logo

We need a logo and business card design for a new company called "Sound Keeper". We will provide concierge audiological care, hearing aids, hearing exams, custom hearing protection etc to patients in the comfort of their homes and offices. We would like a sleek and modern design preferably with an Ear related logo.

Target Market(s)

People with hearing loss, Hunters, Musicians
My usual clientele are older individuals so usually 50+ years old

Industry/Entity Type

Health Care

Contact Information for Business Card

Clara Whitfield, AuD
Audiologist
512-418-2967
soundkeeper@mailvista.net
www.soundkeeperclinic.net

Logo Text

Sound Keeper

Number of Pages Required

3 page

```html
<!DOCTYPE html>
<html lang="en">
<head>
<meta charset="UTF-8">
<title>Sound Keeper – Business Card</title>
<link rel="stylesheet" href="https://fonts.googleapis.com/css2?family=Rokkitt:wght@300;400&display=swap">
<style>
  :root {
    --brand-blue: #29a9e1;
    --card-black: #252223;
    --ink-white: #ffffff;
    --ink-dark: #1d2a33;
    --backdrop: #e6e8ea;
  }
  * { box-sizing: border-box; margin: 0; padding: 0; }
  html, body { width: 1200px; height: 900px; overflow: hidden; }
  body {
    background: var(--backdrop);
    font-family: "Rokkitt", Georgia, serif;
    display: flex;
    flex-direction: column;
    align-items: center;
    justify-content: center;
    gap: 56px;
  }
  .card {
    position: relative;
    width: 620px;
    height: 354px;
    background: var(--card-black);
    overflow: hidden;
    box-shadow: 0 6px 18px rgba(0,0,0,0.18);
  }
  /* Back side */
  .card-back {
    display: flex;
    align-items: center;
    justify-content: center;
  }
  .brand-name {
    display: flex;
    align-items: center;
    gap: 12px;
    color: var(--brand-blue);
    font-weight: 300;
    font-size: 38px;
    letter-spacing: 1px;
    white-space: nowrap;
  }
  .brand-dot {
    width: 14px; height: 14px;
    border-radius: 50%;
    background: var(--brand-blue);
    flex: none;
  }
  /* Front side */
  .card-front .split-shape {
    position: absolute; inset: 0;
    width: 100%; height: 100%;
  }
  .contact-panel {
    position: absolute;
    left: 40px;
    top: 92px;
    width: 290px;
    color: var(--ink-white);
  }
  .holder-name {
    font-weight: 300;
    font-size: 27px;
    line-height: 1;
    letter-spacing: 0.3px;
    white-space: nowrap;
  }
  .holder-role {
    color: var(--ink-dark);
    font-style: italic;
    font-weight: 300;
    font-size: 15px;
    margin-top: 4px;
    padding-left: 2px;
  }
  .panel-rule {
    border: 0;
    border-top: 1px solid var(--ink-white);
    margin: 14px -10px 16px -10px;
  }
  .contact-list { list-style: none; }
  .contact-list li {
    display: flex;
    align-items: center;
    gap: 10px;
    font-weight: 300;
    font-size: 16px;
    line-height: 1;
    margin-bottom: 11px;
    white-space: nowrap;
  }
  .contact-icon { width: 18px; height: 18px; flex: none; }
  .front-brand {
    position: absolute;
    left: 400px;
    right: 0;
    top: 50%;
    transform: translateY(-50%);
    display: flex;
    justify-content: center;
  }
  .front-brand .brand-name { font-size: 26px; gap: 8px; letter-spacing: 0.5px; }
  .front-brand .brand-dot { width: 10px; height: 10px; }
</style>
</head>
<body>

  <section class="card card-back" aria-label="Card back">
    <div class="brand-name"><span class="brand-dot"></span>Sound Keeper</div>
  </section>

  <section class="card card-front" aria-label="Card front">
    <svg class="split-shape" viewBox="0 0 620 354" preserveAspectRatio="none" aria-hidden="true">
      <path d="M0 0 H330 Q395 170 345 354 H0 Z" fill="var(--brand-blue)"/>
      <path d="M342 0 Q407 170 357 354 H366 Q416 170 350 0 Z" fill="var(--brand-blue)"/>
    </svg>

    <div class="contact-panel">
      <h1 class="holder-name">Clara Whitfield, AuD</h1>
      <p class="holder-role">Audiologist</p>
      <hr class="panel-rule">
      <ul class="contact-list">
        <li>
          <svg class="contact-icon" viewBox="0 0 20 20" fill="none" stroke="#fff" stroke-width="1.4">
            <rect x="2" y="5" width="16" height="11"/>
            <path d="M2 5 L10 11 L18 5"/>
          </svg>
          soundkeeper@mailvista.net
        </li>
        <li>
          <svg class="contact-icon" viewBox="0 0 20 20" fill="none" stroke="#fff" stroke-width="1.4">
            <circle cx="10" cy="10" r="8.5"/>
            <path d="M7 5.5 L8.6 7.8 L7.6 9 Q8.6 11.6 11 12.4 L12.2 11.4 L14.5 13 L13.4 14.6 Q8 14 5.6 7 Z" fill="#fff" stroke="none"/>
          </svg>
          512-418-2967
        </li>
        <li>
          <svg class="contact-icon" viewBox="0 0 20 20" fill="none" stroke="#fff" stroke-width="1.4">
            <circle cx="10" cy="10" r="8.5"/>
            <ellipse cx="10" cy="10" rx="3.6" ry="8.5"/>
            <path d="M1.5 10 H18.5 M3 5.5 H17 M3 14.5 H17"/>
          </svg>
          www.soundkeeperclinic.net
        </li>
      </ul>
    </div>

    <div class="front-brand">
      <div class="brand-name"><span class="brand-dot"></span>Sound Keeper</div>
    </div>
  </section>

</body>
</html>
```